Branding for salad and dip containers - retail

we are trying to modernise our packaging design
the lids will be pre-printed (only with our logo) the design can be any shape, preferably not covering the whole top as we want the product to show
NO OTHER details are needed on the lid! Just the logo in bold modern design (using our existing logo and colours) fresh modern and bold
this is the container size we use
https://www.pakbrook.co.uk/acatalog/280ml-rectangular-clear-tamperproof-container-lid.html#SID=64
see images attached of some trials made that we don’t like
1) One has too many other details
2) The other has not utilised our brand and logo

Target Market(s)

Retail Customers

Industry/Entity Type

food

Requirements
Must have
• our current existing logo included
Nice to have
• i would like to see my logo rebranded in a modern sleek design ready to printed on container tops
Should not have
• none of the current add ons- just logo bold and modern

```html
<!DOCTYPE html>
<html lang="en">
<head>
<meta charset="utf-8">
<title>Fernwell's – Lid and Side Labels</title>
<link rel="stylesheet" href="https://fonts.googleapis.com/css2?family=Arvo&display=swap">
<style>
  :root {
    --backdrop: #bde1e5;
    --brand-red: #d51a22;
    --brand-black: #000000;
    --brand-white: #ffffff;
    --cut-guide: #2a9fc6;
  }
  html, body {
    margin: 0;
    padding: 0;
    width: 1200px;
    height: 960px;
    overflow: hidden;
    background: var(--backdrop);
  }
  .artboard {
    display: block;
    width: 1200px;
    height: 960px;
  }
  .fill-backdrop { fill: var(--backdrop); }
  .fill-red { fill: var(--brand-red); }
  .fill-black { fill: var(--brand-black); }
  .cut-guide {
    fill: none;
    stroke: var(--cut-guide);
    stroke-width: 1.6;
  }
  .wordmark {
    fill: var(--brand-white);
    font-family: "Arvo", serif;
    font-weight: 400;
  }
</style>
</head>
<body>
<svg class="artboard" viewBox="0 0 2156 1725" xmlns="http://www.w3.org/2000/svg">
  <defs>
    <clipPath id="lid-shape">
      <circle cx="579" cy="765" r="363"/>
    </clipPath>
    <clipPath id="side-label-shape">
      <rect x="322" y="1173" width="515" height="150"/>
    </clipPath>
  </defs>

  <rect class="fill-backdrop" width="2156" height="1725"/>

  <!-- Lid label -->
  <g class="lid-label" clip-path="url(#lid-shape)">
    <rect class="fill-red" x="200" y="797" width="760" height="340"/>
    <circle class="fill-backdrop" cx="580" cy="720" r="173"/>
    <rect class="fill-black" x="200" y="390" width="760" height="375"/>
    <circle class="fill-black" cx="580" cy="720" r="142"/>
    <circle class="fill-red" cx="580" cy="720" r="113"/>
    <circle class="cut-guide" cx="579" cy="765" r="331"/>
    <text class="wordmark" x="579" y="996" font-size="74" text-anchor="middle">Fernwell's</text>
  </g>

  <!-- Side label -->
  <g class="side-label" clip-path="url(#side-label-shape)">
    <rect class="fill-red" x="423" y="1173" width="414" height="150"/>
    <circle class="fill-backdrop" cx="395" cy="1248" r="55"/>
    <rect class="fill-black" x="322" y="1173" width="89" height="150"/>
    <circle class="fill-black" cx="395" cy="1248" r="43"/>
    <circle class="fill-red" cx="396" cy="1248" r="34"/>
    <rect class="cut-guide" x="331" y="1191" width="494" height="114" rx="14"/>
    <text class="wordmark" x="628" y="1268" font-size="50" text-anchor="middle">Fernwell's</text>
  </g>
</svg>
</body>
</html>
```